Hair salon and Nail salon in Hawaii need a newspaper Ad design.

We need a newspaper Ad design for new open hair & nail salon in Waikiki Hawaii.Our Recommendation service for hair is "Head Spa" $30+tax and for nail is "Manicure Treatment Course" (Filing+Cuticle Care+Massage+Coloring) $20+tax.
We would like to see Hawaiian taste color and also having sense of luxury design. The ad size is W 5.0” x H 6.375”.
I would customers to know the shop place(Lanakila Crest Hotel 1F) , phone(808-555-0173), instagram(salonbrightwave) , our web site https://salonbrightwave.example and recommend services. For Web or Instagram , QR code is acceptable.

Target Market(s)

women & men

Industry/Entity Type

Beauty Salon

Font styles to use
Serif

Colors

Designer to choose colors to be used in the design.

Requirements
Must have
• Tagline for local customers. Shop Name is "SALON BRIGHTWAVE".the shop place(Lanakila Crest Hotel 1F) , phone(808-555-0173), instagram(salonbrightwave) and recommend services.
Nice to have
• Our services are competitive, but we don't want to be seen as just cheap and low quality.

```html
<!DOCTYPE html>
<html lang="en">
<head>
<meta charset="utf-8">
<title>Salon Brightwave – Newspaper Ad</title>
<link rel="stylesheet" href="https://fonts.googleapis.com/css2?family=Playfair+Display:wght@400&family=Questrial&display=swap">
<style>
  :root {
    --ink: #0a0c0d;
    --hair-dark: #1a1310;
    --hair-warm: #3b2a22;
    --skin: #c9a48d;
    --teal: #1f8f8a;
    --teal-band: #2c5f5a;
    --orange: #e58a3c;
    --white: #ffffff;
  }
  * { margin: 0; padding: 0; box-sizing: border-box; }
  html, body { width: 1200px; height: 941px; overflow: hidden; background: var(--ink); }
  .ad {
    position: relative;
    width: 1200px;
    height: 941px;
    overflow: hidden;
    background: var(--ink);
    font-family: "Questrial", "Century Gothic", sans-serif;
    color: var(--white);
  }
  .ad__photo {
    position: absolute;
    inset: 0;
    background:
      radial-gradient(ellipse 420px 560px at 1010px 470px, rgba(201,164,141,0.85) 0%, rgba(150,110,90,0.55) 45%, rgba(59,42,34,0) 75%),
      radial-gradient(ellipse 700px 380px at 560px 230px, rgba(59,42,34,0.85) 0%, rgba(26,19,16,0.6) 55%, rgba(10,12,13,0) 90%),
      linear-gradient(100deg, var(--ink) 0%, var(--hair-dark) 40%, var(--hair-warm) 70%, var(--hair-dark) 100%);
  }
  .brand {
    position: absolute;
    left: 88px;
    top: 75px;
    display: flex;
    align-items: center;
    gap: 18px;
  }
  .brand__mark { width: 106px; height: 111px; background: var(--white); }
  .brand__name { font-size: 25px; letter-spacing: 1px; color: var(--white); margin-top: 22px; }
  .headline {
    position: absolute;
    left: 84px;
    top: 222px;
    font-family: "Playfair Display", Georgia, serif;
    font-weight: 400;
    font-size: 100px;
    line-height: 97px;
    color: var(--white);
  }
  .headline__line { display: block; white-space: nowrap; }
  .headline__line--second { padding-left: 123px; }
  .headline .accent { color: var(--teal); }
  .offer {
    position: absolute;
    left: 85px;
    display: flex;
    align-items: center;
    gap: 25px;
  }
  .offer--spa { top: 455px; }
  .offer--manicure { top: 593px; }
  .price {
    width: 106px;
    height: 106px;
    border: 2px solid var(--orange);
    border-radius: 50%;
    display: flex;
    flex-direction: column;
    align-items: center;
    justify-content: center;
    line-height: 1;
  }
  .price__amount { font-size: 36px; }
  .price__tax { font-size: 15px; margin-top: 2px; }
  .offer__name { font-size: 39px; letter-spacing: 1px; }
  .offer__detail { font-size: 20px; color: var(--teal); margin-top: 6px; }
  .contact-band {
    position: absolute;
    left: 0;
    top: 772px;
    width: 1200px;
    height: 132px;
    background: linear-gradient(90deg, rgba(44,95,90,0.95) 0%, rgba(44,95,90,0.85) 55%, rgba(44,95,90,0) 85%);
  }
  .contact {
    position: absolute;
    display: flex;
    align-items: center;
    gap: 12px;
    font-size: 25px;
    letter-spacing: 0.5px;
  }
  .contact svg { width: 18px; height: 18px; flex: none; }
  .contact--address { left: 90px; top: 807px; }
  .contact--phone { left: 90px; top: 845px; }
  .contact--social { left: 512px; top: 807px; }
  .contact--web { left: 512px; top: 845px; }
</style>
</head>
<body>
<main class="ad">
  <div class="ad__photo" role="img" aria-label="Photo of a woman in profile with long flowing dark brown hair filling the background"></div>

  <header class="brand">
    <div class="brand__mark"></div>
    <span class="brand__name">SALON BRIGHTWAVE</span>
  </header>

  <h1 class="headline">
    <span class="headline__line"><span class="accent">Quality</span> Care</span>
    <span class="headline__line headline__line--second">Quality <span class="accent">Hair</span></span>
  </h1>

  <section class="offer offer--spa">
    <div class="price"><span class="price__amount">$30</span><span class="price__tax">+tax</span></div>
    <div class="offer__text"><div class="offer__name">Head Spa</div></div>
  </section>

  <section class="offer offer--manicure">
    <div class="price"><span class="price__amount">$20</span><span class="price__tax">+tax</span></div>
    <div class="offer__text">
      <div class="offer__name">Manicure Treatment Course</div>
      <div class="offer__detail">(Filing+Cuticle Care+Massage+Coloring)</div>
    </div>
  </section>

  <footer class="contact-band"></footer>

  <div class="contact contact--address">
    <svg viewBox="0 0 24 24" fill="none" stroke="#e58a3c" stroke-width="2"><path d="M12 22s7-7.2 7-12.5A7 7 0 0 0 5 9.5C5 14.8 12 22 12 22z"/><circle cx="12" cy="9.5" r="2.5"/></svg>
    <span>Lanakila Crest Hotel 1F</span>
  </div>
  <div class="contact contact--phone">
    <svg viewBox="0 0 24 24" fill="none" stroke="#e58a3c" stroke-width="2"><path d="M5 3h4l2 5-2.5 1.5a11 11 0 0 0 6 6L16 13l5 2v4a2 2 0 0 1-2 2A17 17 0 0 1 3 5a2 2 0 0 1 2-2z"/></svg>
    <span>808-555-0173</span>
  </div>
  <div class="contact contact--social">
    <svg viewBox="0 0 24 24" fill="none" stroke="#e58a3c" stroke-width="2"><circle cx="12" cy="12" r="8"/></svg>
    <span>salonbrightwave</span>
  </div>
  <div class="contact contact--web">
    <svg viewBox="0 0 24 24" fill="none" stroke="#e58a3c" stroke-width="2"><circle cx="12" cy="12" r="9"/><path d="M3 12h18M12 3c3 3.5 3 14.5 0 18M12 3c-3 3.5-3 14.5 0 18"/></svg>
    <span>salonbrightwave.example</span>
  </div>
</main>
</body>
</html>
```